Harvest Lantern Ministry Conference

I am in need of promotional graphics for our upcoming event. This event, titled "Harbor Crest Youth Conference", is a weekend event for teenagers 11-19 years old. They hear from religious speakers, listen to a band, and do other fun activities. Graphic design should be geared to young adults/older teens. Alcohol, drugs, smoking are not permitted. Open to any color combinations you think fit with your design.
Event Info:
November 1-3, 2024
Tellwood Exhibit Hall, Sioux Falls, SD
Speakers: Marcus Linden (man in light blue shirt in attached photo), Tessa Vandermeer (woman in attached photo), Colin Hardy ( man in dark colored shirt in attached photo)
Worship: KW Collective
HarborCrestGather.com
#742GR
Our Organization Logo (attached): Lumenward
Once designed, I need the following graphics file sizes:
-11x17 Vertical Poster design: include all event info AND a "blank" space on the bottom or box for groups to add their own details/information. Also include the QRV logo and our organization logo Lumenward in some way.
-Make an additional copy of the 11x17 pdf with cut and bleed lines for printing, please.
-4x3 horizontal postcard: include all event info on 1 side including Lumenward logo and QRV; blank backside
-Main Graphic Slide: formatted to fit a widescreen 16x9 screen. Include event name, hashtag, QRV and Lumenward logo
-social media graphic(s) for event: can incorporate some or all of the event details. WILLING TO ADJUST BUDGET FOR SOCIAL MEDIA graphics.
-4.25in x 2.75in vertical badge: include event title on front with Lumenward logo
Target Market
ages 11-19
Target Market(s)
11-19 years old
Industry/Entity Type
Christian Youth Ministry

```html
<!DOCTYPE html>
<html lang="en">
<head>
<meta charset="utf-8">
<title>Harbor Crest Youth Conference – Print Set</title>
<link rel="stylesheet" href="https://fonts.googleapis.com/css2?family=Russo+One&family=Montserrat:wght@400;600;700&display=swap">
<style>
  :root {
    --page: #ffffff;
    --card-grey: #dbe3e8;
    --card-light: #ecf3fa;
    --title-blue: #3a86c0;
    --accent-blue: #2f8fd6;
    --stamp-blue: #3f86aa;
    --stamp-edge: #7fb0c9;
    --ink: #1c1c1c;
    --line-grey: #6f7c84;
    --ribbon-dark: #3b3552;
    --ribbon-gold: #e0c24a;
    --ribbon-pink: #e77aa0;
    --blob-pink: #f08a8a;
    --blob-violet: #7a3cf0;
    --sun-yellow: #f6d21e;
    --halftone-blue: #9cc9f2;
    --figure-blue: #5fb0e6;
    --figure-pink: #f29aa6;
  }
  * { box-sizing: border-box; margin: 0; padding: 0; }
  html, body { width: 1200px; height: 1200px; overflow: hidden; background: var(--page); }
  .canvas { position: relative; width: 1200px; height: 1200px; }
  .card { position: absolute; overflow: hidden; box-shadow: 0 2px 6px rgba(0,0,0,.28); }
  .abs { position: absolute; }
  .title { font-family: "Russo One", "Montserrat", sans-serif; color: var(--title-blue); text-transform: uppercase; }
  .body-text { font-family: "Montserrat", sans-serif; }
  .title, .body-text, .brand-name, .partner-name { z-index: 2; }

  /* decorative fills */
  .ribbon { background: linear-gradient(120deg, var(--ribbon-pink), var(--ribbon-gold) 45%, var(--ribbon-dark)); border-radius: 48% 52% 40% 60% / 60% 40% 60% 40%; opacity: .9; }
  .pink-blob { background: radial-gradient(circle at 40% 40%, var(--blob-pink), #e86aa0 70%, transparent 72%); }
  .corner-mark { background: linear-gradient(160deg, var(--sun-yellow), var(--ribbon-pink) 50%, var(--blob-violet)); border-radius: 40% 60% 50% 50%; }
  .stripes { background: repeating-linear-gradient(180deg, var(--halftone-blue) 0 6px, transparent 6px 9px); border-radius: 0 14px 14px 0; opacity: .85; }
  .halftone { background: radial-gradient(circle, var(--halftone-blue) 0, transparent 70%); opacity: .6; }
  .figure { background: linear-gradient(180deg, var(--figure-pink) 0 18%, var(--figure-blue) 18% 55%, var(--accent-blue) 55%); border-radius: 40%; opacity: .85; }
  .star-glow { background: radial-gradient(circle, #f0a040 0, #9bd49a 35%, transparent 70%); }

  /* postcard back */
  .postcard-back { left: 46px; top: 369px; width: 269px; height: 202px; background: var(--card-grey); }
  .postcard-back .label { left: 20px; top: 28px; font-size: 17px; color: #3b4a52; }
  .postcard-back .divider { left: 135px; top: 35px; width: 1px; height: 137px; background: var(--line-grey); }
  .postcard-back .stamp { left: 206px; top: 25px; width: 46px; height: 59px; background: var(--stamp-blue); border: 3px solid var(--stamp-edge); }
  .postcard-back .address-line { left: 153px; width: 98px; height: 1px; background: var(--line-grey); }
  .postcard-back .from { left: 24px; top: 137px; font-size: 9px; color: #3b4a52; }
  .postcard-back .from-line { left: 25px; top: 167px; width: 92px; height: 1px; background: var(--line-grey); }

  /* postcard front */
  .postcard-front { left: 46px; top: 629px; width: 269px; height: 203px; background: var(--card-grey); }
  .postcard-front .title { left: 13px; top: 31px; font-size: 16px; line-height: 17.5px; }
  .postcard-front .tagline { left: 13px; top: 85px; font-size: 4.6px; font-weight: 700; line-height: 6px; color: var(--ink); }
  .brand-name { font-family: "Montserrat", sans-serif; font-weight: 700; color: var(--accent-blue); }
  .partner-name { font-family: "Montserrat", sans-serif; font-weight: 700; color: var(--ink); }

  /* poster */
  .poster { left: 416px; top: 345px; width: 327px; height: 504px; background: var(--card-light); }
  .poster .title { left: 32px; top: 75px; font-size: 23px; line-height: 25.5px; }
  .poster .tagline { right: 33px; top: 316px; font-size: 10.5px; font-weight: 700; line-height: 13px; text-align: right; color: var(--ink); }
  .poster .event-facts { right: 31px; top: 358px; font-size: 6.6px; font-weight: 600; letter-spacing: 2.2px; line-height: 9px; text-align: right; color: var(--accent-blue); }
  .poster .worship { right: 33px; top: 389px; font-size: 5.6px; line-height: 8.5px; text-align: right; color: var(--ink); }
  .poster .group-box { left: 199px; top: 410px; width: 140px; height: 28px; background: #fff; border-radius: 14px; padding: 3px 18px 0 0; font-size: 5.6px; line-height: 9px; text-align: right; color: var(--ink); }
  .speaker { top: 390px; width: 58px; text-align: center; }
  .speaker .portrait { width: 49px; height: 49px; margin: 0 auto; border-radius: 50%; background: linear-gradient(160deg, #c9d6df, #7b8a96); }
  .speaker .name { margin-top: 9px; font-size: 5.4px; font-weight: 700; letter-spacing: 1.4px; line-height: 9px; color: var(--ink); text-transform: uppercase; }

  /* badge */
  .badge { left: 822px; top: 345px; width: 332px; height: 512px; background: var(--card-light); }
  .badge .brand-name { left: 0; width: 100%; top: 98px; text-align: center; font-size: 34px; }
  .badge .title { left: 0; width: 100%; top: 209px; font-size: 34px; line-height: 37.5px; text-align: center; }
</style>
</head>
<body>
<main class="canvas">

  <section class="card postcard-back" aria-label="Postcard back">
    <p class="abs label body-text">Postcard</p>
    <div class="abs divider"></div>
    <div class="abs stamp"></div>
    <div class="abs address-line" style="top:104px"></div>
    <div class="abs address-line" style="top:125px"></div>
    <div class="abs address-line" style="top:146px"></div>
    <div class="abs address-line" style="top:167px"></div>
    <p class="abs from body-text">From :</p>
    <div class="abs from-line"></div>
  </section>

  <section class="card postcard-front" aria-label="Postcard front">
    <div class="abs pink-blob" style="left:200px;top:88px;width:72px;height:58px" role="img" aria-label="Pink gradient blob"></div>
    <div class="abs ribbon" style="left:-10px;top:158px;width:120px;height:55px" role="img" aria-label="Iridescent ribbon"></div>
    <div class="abs ribbon" style="left:175px;top:135px;width:105px;height:78px" role="img" aria-label="Iridescent ribbon"></div>
    <div class="abs" style="left:85px;top:168px;width:100px;height:40px;background:radial-gradient(ellipse at 60% 70%,var(--blob-violet),#b7a2f5 70%,transparent 72%)" role="img" aria-label="Violet halftone cloud"></div>
    <div class="abs stripes" style="left:0;top:100px;width:19px;height:36px" role="img" aria-label="Blue halftone stripes"></div>
    <div class="abs" style="left:238px;top:-6px;width:40px;height:54px;border-radius:50%;background:var(--sun-yellow)" role="img" aria-label="Yellow sun shape"></div>
    <div class="abs figure" style="left:140px;top:112px;width:48px;height:58px" role="img" aria-label="Illustration of a striding teen in a pink hat and blue outfit"></div>
    <h2 class="abs title">Harbor Crest<br>Youth<br>Conference</h2>
    <p class="abs tagline body-text">A weekend of inspiration, music,<br>and fun for teens 11-19</p>
    <span class="abs brand-name" style="left:170px;top:51px;font-size:8px">Lumenward</span>
    <span class="abs partner-name" style="left:230px;top:48px;font-size:12px">QRV</span>
  </section>

  <section class="card poster" aria-label="Event poster">
    <div class="abs corner-mark" style="left:3px;top:15px;width:45px;height:55px" role="img" aria-label="Gradient looping mark"></div>
    <div class="abs halftone" style="left:205px;top:60px;width:120px;height:110px" role="img" aria-label="Blue halftone dot pattern"></div>
    <div class="abs stripes" style="left:0;top:148px;width:60px;height:54px" role="img" aria-label="Blue halftone stripes"></div>
    <div class="abs pink-blob" style="left:280px;top:185px;width:60px;height:85px" role="img" aria-label="Pink gradient blob"></div>
    <div class="abs ribbon" style="left:250px;top:205px;width:85px;height:100px" role="img" aria-label="Iridescent ribbon"></div>
    <div class="abs ribbon" style="left:-10px;top:300px;width:110px;height:80px" role="img" aria-label="Iridescent ribbon"></div>
    <div class="abs figure" style="left:70px;top:155px;width:150px;height:160px" role="img" aria-label="Illustration of a striding teen in a pink hat and blue outfit"></div>
    <span class="abs brand-name" style="left:250px;top:38px;font-size:11px">Lumenward</span>
    <h1 class="abs title">Harbor Crest<br>Youth<br>Conference</h1>
    <p class="abs tagline body-text">A WEEKEND OF<br>INSPIRATION, MUSIC, AND<br>FUN FOR TEENS 11-19</p>
    <p class="abs event-facts body-text">NOVEMBER 1-3, 2024<br>TELLWOOD EXHIBIT HALL,<br>SIOUX FALLS, SD</p>
    <p class="abs worship body-text">Worship: KW Collective<br>HarborCrestGather.com</p>
    <div class="abs group-box body-text">Add<br>Details/information</div>
    <div class="abs speaker body-text" style="left:18px">
      <div class="portrait" role="img" aria-label="Portrait of speaker Marcus Linden"></div>
      <p class="name">Marcus<br>Linden</p>
    </div>
    <div class="abs speaker body-text" style="left:79px">
      <div class="portrait" role="img" aria-label="Portrait of speaker Tessa Vandermeer"></div>
      <p class="name">Tessa<br>Vandermeer</p>
    </div>
    <div class="abs speaker body-text" style="left:142px">
      <div class="portrait" role="img" aria-label="Portrait of speaker Colin Hardy"></div>
      <p class="name">Colin<br>Hardy</p>
    </div>
    <span class="abs partner-name" style="left:266px;top:453px;font-size:16px">QRV</span>
    <div class="abs stripes" style="left:161px;top:473px;width:96px;height:31px;border-radius:14px" role="img" aria-label="Blue halftone stripes"></div>
  </section>

  <section class="card badge" aria-label="Event badge">
    <div class="abs corner-mark" style="left:0;top:0;width:70px;height:86px" role="img" aria-label="Gradient looping mark"></div>
    <div class="abs star-glow" style="left:240px;top:125px;width:92px;height:108px" role="img" aria-label="Soft glowing star"></div>
    <div class="abs pink-blob" style="left:272px;top:345px;width:68px;height:92px" role="img" aria-label="Pink gradient blob"></div>
    <div class="abs ribbon" style="left:-10px;top:395px;width:125px;height:88px" role="img" aria-label="Iridescent ribbon"></div>
    <div class="abs corner-mark" style="left:116px;top:445px;width:44px;height:54px" role="img" aria-label="Small gradient blob"></div>
    <div class="abs ribbon" style="left:228px;top:425px;width:110px;height:85px" role="img" aria-label="Iridescent ribbon"></div>
    <span class="abs brand-name">Lumenward</span>
    <h2 class="abs title">Harbor<br>Crest<br>Youth<br>Conference</h2>
  </section>

</main>
</body>
</html>
```